ちょっと急いでおりまして、
当方デザインをする時間がないので、
アウトソーシングしたいと思います。

文章、と構成だけを作りましたので、
宜しければ、お願い致します。

TAVELIA JAPAN で使用する、
お客さまにブランディングするための、
青嶺かやどり の パンフレットです。

PDFで、説明文を記載致しますので、
また見ておいて下さい。

画像素材も、添付させて頂きます。
「青嶺かやどり・かやたまご」を使うフォントは、
明朝体です。アウトラインしたデータも
添付いたします。それを活用下さい。

A4サイズ (裏・表)
両面カラーでで作っていただけると幸いです。

※もしかすると、A0サイズで引き伸ばしてつかうかもしれません。
どうぞよろしくお願い致します。

何か御不明な点がございましたら、お気軽に
ご質問ください。

当社青嶺かやどりの商品ページです。
参考にして下さい。
http://item.shopmarket-example.jp/poultry-hoshino/20004681/

青嶺かやどり協議会の ページです。
http://www.kayadori-example.com/
素材を添付いたします。レイヤーを使っておりますので、分解してください。
このページにある

の画像のような感じで、要約していただけると
幸いです。
画像を追加いたしました。
タイトルが、4Aに なってました。

すみません。A4ポスターです。
循環型の 111 のような 感じで、

ぐるっと 回る ように わかりやすく つくって頂けると幸いです。
かやどりの アニメーションデータは、

aiファイル イラストレーターの
かやたまご に 入っています。

レイヤーで組んでいますが、それを修正して作って下さい。
素材 画像を追加いたしました。
素材追加いたします。

111、222、333、444画像は、見本画像です。
イメージの参考になるかも?と思いまして、
かやどり からでる 副産物の 鶏糞堆肥もっこもこ の画像を 追加いたします。

裏側の、一番重要な情報を綺麗にまとめてくださりました。
そして、私達が やっていることに対して 共感頂けたことが大きかったです。
少し修正頂きたい部分がありますので、御連絡頂けると幸いです。

皆様 急な対応、ありがとうございます。
10件も御応募いただけるとは思っても居なかったのと、
そして、みなさんからの提案が本当に良かったので。
こちらとしても 悩ましかったです。
御提案くださった皆様。本当に、ありがとうございましたm(__)m

```html
<!DOCTYPE html>
<html lang="ja">
<head>
<meta charset="utf-8">
<title>青嶺かやどり ポスター</title>
<link rel="stylesheet" href="https://fonts.googleapis.com/css2?family=Shippori+Mincho:wght@700;800&family=Zen+Maru+Gothic:wght@500;700&display=swap">
<style>
:root{
  --red:#c4122f;
  --deep:#9e0c24;
  --pink:#f2a7bb;
  --pink-soft:#fbdbe4;
  --pink-pale:#fff1f5;
  --gold:#d9a63a;
  --photo-compost:#c99a5b;
  --photo-person:#7d8a6a;
  --ink:#4a2b30;
  --white:#ffffff;
}
*{margin:0;padding:0;box-sizing:border-box}
html,body{width:856px;height:1200px;overflow:hidden;background:var(--white)}
.poster{position:relative;width:856px;height:1200px;overflow:hidden;
  font-family:"Zen Maru Gothic",sans-serif;color:var(--ink);
  background:linear-gradient(180deg,var(--white) 0,var(--pink-pale) 60%,var(--pink-soft) 100%)}
.blossom{position:absolute;border-radius:50%;background:radial-gradient(circle,#f7c3d2,#ee93ab)}
.title{position:absolute;left:0;right:0;top:40px;text-align:center;
  font-family:"Shippori Mincho",serif;font-weight:800;font-size:104px;color:var(--red);letter-spacing:10px}
.mascot-note{position:absolute;right:26px;top:34px;width:110px;font-size:15px;line-height:1.35;color:var(--red);
  writing-mode:vertical-rl;height:110px}
.subtitle-band{position:absolute;left:40px;right:40px;top:186px;height:52px;border-radius:26px;
  background:linear-gradient(90deg,var(--pink-soft),var(--pink),var(--pink-soft));
  text-align:center;font-family:"Shippori Mincho",serif;font-weight:700;font-size:30px;line-height:52px;color:var(--deep)}
.cycle{position:absolute;left:0;top:250px;width:600px;height:500px}
.cycle svg{position:absolute;left:0;top:0}
.mascot{position:absolute;left:225px;top:170px;width:150px;height:130px;border-radius:50%;
  background:radial-gradient(circle at 45% 40%,#ffffff,#f6dde4)}
.step-num{position:absolute;width:44px;height:44px;border-radius:50%;background:var(--red);color:var(--white);
  font-weight:700;font-size:24px;text-align:center;line-height:44px}
.step-text{position:absolute;width:118px;font-size:13px;line-height:1.4;color:var(--ink)}
.compost-photo{position:absolute;left:586px;top:262px;width:230px;height:230px;border-radius:50%;
  background:radial-gradient(circle at 40% 35%,#e2be86,var(--photo-compost) 60%,#8c6236);border:6px solid var(--white)}
.compost-label{position:absolute;left:600px;top:500px;font-family:"Shippori Mincho",serif;font-weight:800;font-size:26px;color:var(--red);line-height:1.25}
.person-photo{position:absolute;left:584px;top:582px;width:130px;height:160px;background:linear-gradient(180deg,#aeb89a,var(--photo-person));border:5px solid var(--white)}
.person-caption{position:absolute;left:724px;top:584px;width:112px;font-size:12.5px;line-height:1.45}
.person-caption b{display:block;font-size:15px;color:var(--red);margin-bottom:4px}
.badge{position:absolute;left:28px;width:118px;height:118px;border-radius:50%}
.badge.gold{top:800px;background:radial-gradient(circle,#f4d27a,var(--gold))}
.badge.rose{top:950px;background:radial-gradient(circle,#f8c4d2,#e07c98)}
.lead{position:absolute;left:168px;top:790px;width:660px;font-weight:700;color:var(--red);font-size:17px;line-height:1.6}
.lead .big{font-size:22px}
.info-box{position:absolute;left:168px;top:905px;width:660px;height:200px;background:var(--white);border-radius:14px;
  border:3px solid var(--pink);padding:16px 22px;font-size:16px;line-height:1.7}
.info-box h2{font-size:20px;color:var(--red);margin-bottom:6px}
.info-box li{list-style:none}
.info-box li::before{content:"●";color:var(--pink);margin-right:6px}
.footer-note{position:absolute;left:168px;right:28px;top:1120px;font-size:17px;font-weight:700;color:var(--deep);line-height:1.6}
</style>
</head>
<body>
<main class="poster">
  <div class="blossom" style="left:18px;top:20px;width:70px;height:70px" role="img" aria-label="梅の花の飾り"></div>
  <div class="blossom" style="left:70px;top:110px;width:40px;height:40px" role="img" aria-label="梅の花の飾り"></div>
  <div class="blossom" style="left:640px;top:120px;width:46px;height:46px" role="img" aria-label="梅の花の飾り"></div>
  <h1 class="title">青嶺かやどり</h1>
  <p class="mascot-note">地域のみんなで育てました</p>
  <div class="subtitle-band">地球に優しい青嶺かやどりの取り組み</div>

  <section class="cycle">
    <svg width="600" height="500" viewBox="0 0 600 500">
      <defs><marker id="arrow" markerWidth="10" markerHeight="10" refX="5" refY="5" orient="auto"><path d="M0,0 L10,5 L0,10 z" fill="#f2a7bb"/></marker></defs>
      <circle cx="300" cy="235" r="180" fill="#fff7f9" stroke="#f2a7bb" stroke-width="10" stroke-dasharray="60 22"/>
      <path d="M300 55 A180 180 0 0 1 441 122" fill="none" stroke="#f2a7bb" stroke-width="4" marker-end="url(#arrow)"/>
    </svg>
    <div class="mascot" role="img" aria-label="かやどりのキャラクターイラスト"></div>
    <div class="step-num" style="left:278px;top:30px">1</div>
    <div class="step-num" style="left:420px;top:98px">2</div>
    <div class="step-num" style="left:454px;top:248px">3</div>
    <div class="step-num" style="left:356px;top:372px">4</div>
    <div class="step-num" style="left:200px;top:372px">5</div>
    <div class="step-num" style="left:102px;top:248px">6</div>
    <div class="step-num" style="left:136px;top:98px">7</div>
    <p class="step-text" style="left:242px;top:80px;text-align:center">梅を食べた<br>かやどり誕生</p>
    <p class="step-text" style="left:470px;top:140px">鶏が出す糞を<br>堆肥化して<br>鶏糞堆肥に</p>
    <p class="step-text" style="left:478px;top:300px">その堆肥を<br>梅畑に散布</p>
    <p class="step-text" style="left:372px;top:424px">梅畑の土が<br>ふかふかに育つ</p>
    <p class="step-text" style="left:160px;top:424px">収穫した梅を<br>梅干しに加工</p>
    <p class="step-text" style="left:10px;top:300px">梅酢を飼料に<br>混ぜて<br>かやどりへ</p>
    <p class="step-text" style="left:20px;top:140px">梅の香りで<br>健康に<br>育ちます</p>
  </section>

  <div class="compost-photo" role="img" aria-label="鶏糞堆肥の写真"></div>
  <p class="compost-label">鶏糞堆肥<br>「もっこもこ」</p>
  <div class="person-photo" role="img" aria-label="組合員の写真"></div>
  <p class="person-caption"><b>組合員 星野 健太</b>かやどりの鶏糞は堆肥となって畑へ戻り、また新しい梅を育てます。</p>

  <div class="badge gold" role="img" aria-label="受賞の記章"></div>
  <div class="badge rose" role="img" aria-label="受賞の記章"></div>
  <p class="lead"><span class="big">梅の組合員が育てた青嶺かやどり</span><br>鶏糞堆肥もっこもこ　好評販売中<br>青嶺かやどり協議会が品質を守っています</p>
  <div class="info-box">
    <h2>女性の目線から優しい鶏ブランド</h2>
    <ul>
      <li>梅酢入りの飼料でのびのび育てています</li>
      <li>鶏糞は堆肥にして畑へ返しています</li>
      <li>かやたまごもあわせてお楽しみください</li>
      <li>地域の循環で安心をお届けします</li>
    </ul>
  </div>
  <p class="footer-note">青嶺かやどり・かやたまごは、地球にやさしい循環から生まれています。</p>
</main>
</body>
</html>
```